Vex

I have the logo for the back already. Need the front to match.
Need a VEX logo which I can provide or you can download one - VEX Realty in canada... Back of the card will be my logo and name. Front will have the info...
I would like a black background. Match colors on front to the back..
Details on Card

Target Market(s)

Realestate clients.. Keep it classy like the logo

Contact Information for Business Card

Moren Tadwick office - 5817730264 cell - 5819063147 email - Moren@MorenTadwick.Com. website - MorenTadwick.Com Facebook - MTadwRealty Instagram - Moren_Qpl_Realtor Address - 418 - 23 St NE | K5P2M8

Colors
3176b5
33a6d7
85cae6

Requirements
Must have
• same color scheme as the logo
logo will be on the back
Black Background
Horizontal card
The one side of the card should be clean. like I stated, just my logo " Moren Tadwick " and nothing else

```html
<!DOCTYPE html>
<html lang="en">
<head>
<meta charset="utf-8">
<title>Moren Tadwick – Business Card</title>
<link href="https://fonts.googleapis.com/css2?family=Lato:ital,wght@0,400;0,700;0,900;1,400&display=swap" rel="stylesheet">
<style>
  :root {
    --stage: #262626;
    --card: #151515;
    --card-edge: #1d1d1d;
    --blue: #1f70be;
    --silver: #c9ccd0;
    --white: #f4f4f4;
    --muted: #e2e2e2;
  }
  * { margin: 0; padding: 0; box-sizing: border-box; }
  html, body {
    width: 1200px; height: 900px; overflow: hidden;
    background: var(--stage);
    font-family: "Lato", sans-serif;
  }
  .stage {
    width: 1200px; height: 900px;
    display: flex; flex-direction: column;
    align-items: center; justify-content: center; gap: 40px;
  }
  .card {
    position: relative;
    width: 700px; height: 400px;
    background: linear-gradient(160deg, var(--card-edge), var(--card) 60%);
    box-shadow: 0 14px 30px rgba(0,0,0,.55);
    overflow: hidden;
  }
  /* logo side */
  .card--brand .accent {
    position: absolute; height: 10px; width: 210px; background: var(--blue);
  }
  .card--brand .accent--top { top: 0; left: 0; }
  .card--brand .accent--bottom { bottom: 0; right: 0; }
  .brand-mark {
    position: absolute; inset: 0;
    display: flex; align-items: center; justify-content: center; gap: 18px;
  }
  .brand-mark__dot {
    width: 14px; height: 14px; background: var(--blue);
  }
  .brand-mark__name {
    color: var(--blue);
    font-weight: 700; font-size: 46px; letter-spacing: 3px;
  }
  /* info side */
  .info {
    position: absolute; top: 62px; left: 0; right: 0;
    text-align: center; color: var(--muted);
  }
  .info__name {
    color: var(--white);
    font-weight: 900; font-size: 34px; letter-spacing: 3px;
  }
  .info__address {
    margin-top: 26px; font-size: 17px;
  }
  .info__rule {
    width: 70px; height: 2px; background: var(--blue);
    margin: 14px auto 18px;
  }
  .info__line {
    font-size: 16px; line-height: 30px;
  }
  .info__line span + span { margin-left: 14px; }
  .info__label { color: var(--blue); font-style: italic; }
  .band {
    position: absolute; left: 0; right: 0; bottom: 0; height: 16px;
    background: var(--blue);
    border-top: 2px solid var(--silver);
  }
</style>
</head>
<body>
<main class="stage">
  <section class="card card--brand">
    <div class="accent accent--top"></div>
    <div class="brand-mark">
      <span class="brand-mark__dot"></span>
      <span class="brand-mark__name">MOREN TADWICK</span>
    </div>
    <div class="accent accent--bottom"></div>
  </section>

  <section class="card card--info">
    <div class="info">
      <h1 class="info__name">MOREN TADWICK</h1>
      <p class="info__address">418 - 23 St NE | K5P2M8</p>
      <div class="info__rule"></div>
      <p class="info__line">
        <span><span class="info__label">T:</span> 5817730264 (office)</span>
        <span><span class="info__label">M:</span> 5819063147</span>
      </p>
      <p class="info__line">
        <span><span class="info__label">E:</span> Moren@MorenTadwick.Com</span>
        <span><span class="info__label">W:</span> MorenTadwick.Com</span>
      </p>
      <p class="info__line">
        <span><span class="info__label">F:</span> MTadwRealty</span>
        <span><span class="info__label">I:</span> Moren_Qpl_Realtor</span>
      </p>
    </div>
    <div class="band"></div>
  </section>
</main>
</body>
</html>
```